Creative Web Design - Intl Market Research Company

We need an innovative web design for an emerging company into the international market research marketplace.

The company, Halvenor Associates, is a Trade, Investment, and Market Research company. Halvenor offers domestic and international companies increased success in the U.S. marketplace by providing a variety of services. (seen on attached brochure)

The website should be cutting edge and creative while having an easy navigation. The color is not fixed and attached logo is not finalized, feel free to post anything from conservative to progressive options. Keep in mind target customers are domestic and international businesses looking to emerge/improve in the U.S. marketplace.

Additional Company information is located in the attached documentation. The documentation is outdated & winner will have priority standing for our next projects.(logo & document re-design)

I have received a few e-mail requests and have updated the status to guaranteed payment.

Thanks!

Target Market(s)

Any company, foreign and domestic, looking to introduce their product into the U.S. marketplace.

Industry/Entity Type

Market Research

Requirements
Must have
• Easy Navigation
Should not have
• Too many buttons
Difficult navigation
Excessive Typography

```html
<!DOCTYPE html>
<html lang="en">
<head>
<meta charset="utf-8">
<title>Halvenor Associates — Trade, Investment, Market Research</title>
<link rel="stylesheet" href="https://fonts.googleapis.com/css2?family=Raleway:wght@300;400;500;700&family=Yellowtail&family=Arvo&family=Lato:wght@400;700&display=swap">
<style>
:root{
  --ink:#1c1c1c;
  --text:#333333;
  --muted:#777777;
  --gold:#c9a233;
  --gold-light:#f2d56a;
  --gold-dark:#8a6a12;
  --band:#e9e7e2;
  --panel:#efeeea;
  --rule:#d6d4cf;
  --footer:#0b0b0b;
  --paper:#ffffff;
}
*{margin:0;padding:0;box-sizing:border-box}
html,body{width:1084px;height:1200px;overflow:hidden;background:var(--paper)}
body{position:relative;font-family:"Raleway",Arial,sans-serif;color:var(--text)}
.abs{position:absolute}

/* header */
.brand-name{left:166px;top:22px;font-family:"Raleway",Arial,sans-serif;font-weight:700;font-size:36px;color:var(--ink);letter-spacing:.5px;white-space:nowrap}
.brand-globes{left:228px;top:66px;width:186px;height:92px;z-index:3}
.social{left:816px;top:28px;display:flex;gap:10px}
.social span{width:20px;height:20px;border-radius:3px;background:#666}
.tagline{left:528px;top:68px;font-family:"Arvo",Georgia,serif;font-size:20px;letter-spacing:1px;color:var(--ink);white-space:nowrap}
.nav-band{left:0;top:108px;width:1084px;height:37px;background:var(--band);border-top:1px solid #dcdad4;border-bottom:1px solid #dcdad4}
.nav{left:443px;top:118px;display:flex;font-size:14px;font-weight:500;color:var(--ink);white-space:nowrap}
.nav a{color:inherit;text-decoration:none}
.nav .sep{margin:0 13px}

/* hero */
.backdrop{left:72px;top:146px;width:940px;height:460px;border-radius:50%;background:radial-gradient(ellipse at center,#f4f4f2 0%,#fafaf9 60%,#ffffff 100%);opacity:.9}
.hero{left:0;top:212px;width:1084px;text-align:center;color:var(--ink);font-size:46px;line-height:54px;font-weight:300;letter-spacing:.5px}
.hero strong{font-weight:700}
.steps-panel{left:163px;top:476px;width:759px;height:116px;background:var(--panel);border-bottom:2px solid var(--rule);box-shadow:0 1px 2px rgba(0,0,0,.08)}
.step{width:182px;text-align:center;top:400px}
.step svg{display:block;margin:0 auto}
.step p{margin-top:10px;font-size:18px;line-height:20px;color:#444}

/* intro + services */
.script-head{font-family:"Yellowtail",cursive;font-size:34px;color:var(--ink);white-space:nowrap}
.intro-head{left:188px;top:628px}
.intro{left:188px;top:686px;width:350px;font-size:15.5px;line-height:21.6px;color:var(--text)}
.services-head{left:554px;top:628px}
.services-lead{left:554px;top:670px;font-size:15.5px;font-weight:500;color:var(--ink)}
.list{font-size:15.5px;line-height:21.6px;color:var(--muted);list-style:none}
.list-a{left:554px;top:691px}
.list-b{left:757px;top:691px;width:170px}

/* partner strip */
.partners{left:170px;top:817px;width:749px;height:71px;border:1px solid var(--rule);background:linear-gradient(#ffffff,#f4f4f4);display:flex;align-items:center;justify-content:space-around;padding:0 14px}
.partners span{display:block;height:22px;background:#d4d4d4;border-radius:3px}
.partners .round{width:36px;height:36px;border-radius:50%}

/* news + testimonials */
.news-head{left:180px;top:914px}
.testi-head{left:596px;top:914px}
.btn{width:69px;height:20px;border-radius:3px;background:linear-gradient(var(--gold-light),var(--gold) 55%,var(--gold-dark));color:var(--ink);font-family:"Lato",Arial,sans-serif;font-size:11px;font-weight:700;text-align:center;line-height:20px;box-shadow:0 1px 2px rgba(0,0,0,.3)}
.news-more{left:443px;top:928px}
.testi-more{left:829px;top:928px}
.date{width:30px;height:28px;border:2px solid #555;text-align:center;font-family:"Lato",Arial,sans-serif;color:#333}
.date b{display:block;font-size:13px;line-height:14px;margin-top:2px}
.date i{display:block;font-style:normal;font-size:5px;letter-spacing:.5px}
.news-text{font-family:"Lato",Arial,sans-serif;font-size:10px;line-height:16px;color:#333;width:290px}
.quote{left:590px;top:972px;width:309px;height:98px;border:2px solid #e1e1e1;border-radius:8px;background:#fff;padding:10px 12px;font-family:"Lato",Arial,sans-serif;font-size:10px;line-height:16px;color:#333}
.quote cite{display:block;margin-top:6px;font-family:Georgia,serif;font-style:normal;font-weight:700;font-size:10px;color:#888}
.quote-tail{left:852px;top:1068px}

/* footer */
.footer{left:0;top:1111px;width:1084px;height:89px;background:linear-gradient(var(--footer) 70%,#222)}
.footer-links{left:180px;top:1128px;font-family:"Lato",Arial,sans-serif;font-size:10px;color:#bbb;white-space:nowrap}
.footer-links .sep{margin:0 6px}
.copyright{left:180px;top:1153px;font-family:"Lato",Arial,sans-serif;font-size:10px;color:#ccc;white-space:nowrap}
.footer-globes{left:782px;top:1083px;width:122px;height:60px}
.footer-name{left:610px;top:1146px;font-family:"Raleway",Arial,sans-serif;font-weight:700;font-size:26px;color:#fff;white-space:nowrap}
</style>
</head>
<body>
<svg width="0" height="0" class="abs" aria-hidden="true">
  <defs>
    <linearGradient id="gold" x1="0" y1="0" x2="1" y2="1">
      <stop offset="0" stop-color="#f6dc74"/>
      <stop offset=".5" stop-color="#c9a233"/>
      <stop offset="1" stop-color="#7a5c10"/>
    </linearGradient>
    <radialGradient id="globe" cx=".4" cy=".4" r=".7">
      <stop offset="0" stop-color="#d9c27a"/>
      <stop offset=".7" stop-color="#8a7a3a"/>
      <stop offset="1" stop-color="#4a3f1a"/>
    </radialGradient>
  </defs>
</svg>

<header>
  <div class="abs brand-name">Halvenor Associates</div>
  <svg class="abs brand-globes" viewBox="0 0 186 92" role="img" aria-label="Pair of antique globe illustrations">
    <circle cx="46" cy="46" r="43" fill="url(#globe)" stroke="#c9a233" stroke-width="4"/>
    <circle cx="140" cy="46" r="43" fill="url(#globe)" stroke="#c9a233" stroke-width="4"/>
  </svg>
  <div class="abs social" aria-label="Social links"><span></span><span></span><span></span><span></span></div>
  <div class="abs tagline">TRADE,INVESTMENT,MARKET RESEARCH</div>
  <div class="abs nav-band"></div>
  <nav class="abs nav">
    <a href="#">HOME</a><span class="sep">/</span>
    <a href="#">ABOUT</a><span class="sep">/</span>
    <a href="#">BLOG</a><span class="sep">/</span>
    <a href="#">CONTACT US</a><span class="sep">/</span>
    <a href="#">REQUEST QUOTE</a>
  </nav>
</header>

<main>
  <div class="abs backdrop" role="img" aria-label="Faint antique world map in two hemispheres"></div>
  <h1 class="abs hero">MEETING YOUR<br><strong>BUSINESS INFORMATION NEEDS</strong><br>ACROSS THE GLOBE.</h1>

  <div class="abs steps-panel"></div>
  <div class="abs step" style="left:172px">
    <svg width="125" height="125" viewBox="0 0 125 125" aria-hidden="true">
      <circle cx="62.5" cy="62.5" r="62.5" fill="#000"/>
      <circle cx="62.5" cy="62.5" r="46" fill="none" stroke="url(#gold)" stroke-width="7"/>
      <circle cx="62.5" cy="62.5" r="30" fill="none" stroke="url(#gold)" stroke-width="7"/>
      <circle cx="62.5" cy="62.5" r="14" fill="url(#gold)"/>
    </svg>
    <p>Research<br>Appropriate Firms</p>
  </div>
  <div class="abs step" style="left:354px">
    <svg width="125" height="125" viewBox="0 0 125 125" aria-hidden="true">
      <circle cx="62.5" cy="62.5" r="62.5" fill="#000"/>
      <path d="M30 32V92H96" fill="none" stroke="url(#gold)" stroke-width="6"/>
      <path d="M38 80L54 58L68 70L88 44" fill="none" stroke="url(#gold)" stroke-width="6" stroke-linejoin="round"/>
      <path d="M78 38L96 34L92 52Z" fill="url(#gold)"/>
    </svg>
    <p>Present Your<br>Product/Service</p>
  </div>
  <div class="abs step" style="left:537px">
    <svg width="125" height="125" viewBox="0 0 125 125" aria-hidden="true">
      <circle cx="62.5" cy="62.5" r="62.5" fill="#000"/>
      <g fill="none" stroke="url(#gold)" stroke-width="5">
        <circle cx="62.5" cy="62.5" r="42"/>
        <ellipse cx="62.5" cy="62.5" rx="20" ry="42"/>
        <line x1="62.5" y1="20" x2="62.5" y2="105"/>
        <line x1="21" y1="62.5" x2="104" y2="62.5"/>
        <path d="M28 42H97M28 83H97"/>
      </g>
    </svg>
    <p>Select Potential<br>Matches</p>
  </div>
  <div class="abs step" style="left:720px">
    <svg width="125" height="125" viewBox="0 0 125 125" aria-hidden="true">
      <circle cx="62.5" cy="62.5" r="62.5" fill="#000"/>
      <circle cx="62.5" cy="66" r="32" fill="none" stroke="url(#gold)" stroke-width="5"/>
      <circle cx="62.5" cy="30" r="15" fill="url(#gold)"/>
      <circle cx="32" cy="82" r="15" fill="url(#gold)"/>
      <circle cx="93" cy="82" r="15" fill="url(#gold)"/>
    </svg>
    <p>Introduce You to<br>Companies</p>
  </div>

  <h2 class="abs script-head intro-head">Halvenor Associates</h2>
  <p class="abs intro">The world is fast becoming a global economy and businesses wanting to succeed in this highly competitive environment must have access to upto-date business information.</p>

  <h2 class="abs script-head services-head">List Services</h2>
  <p class="abs services-lead">Fast and Accurate Lists of:</p>
  <ul class="abs list list-a">
    <li>* Importers</li>
    <li>* Agents/Representatives</li>
    <li>* Distributors</li>
    <li>* Manufacturers</li>
  </ul>
  <ul class="abs list list-b">
    <li>* Joint Venture Partners</li>
    <li>* Manufacturing Under License Partners</li>
    <li>* Investment Partners</li>
  </ul>

  <div class="abs partners" aria-label="Partner badges">
    <span style="width:128px"></span>
    <span style="width:96px"></span>
    <span class="round"></span>
    <span style="width:92px"></span>
    <span style="width:112px"></span>
    <span style="width:100px"></span>
  </div>

  <h2 class="abs script-head news-head">News/Event</h2>
  <div class="abs btn news-more">View All</div>
  <div class="abs date" style="left:184px;top:980px"><b>20</b><i>FEB</i></div>
  <p class="abs news-text" style="left:236px;top:978px">Lorem ipsum dolor sit amet, consectetuer adipiscing elit, sed diam nonummy nibh euismod tincidunt ut laoreet dolore magna.</p>
  <div class="abs date" style="left:184px;top:1035px"><b>20</b><i>FEB</i></div>
  <p class="abs news-text" style="left:236px;top:1033px;width:300px">Lorem ipsum dolor sit amet, consectetuer adipiscing elit, sed diam nonummy nibh euismod tincidunt ut laoreet dolore magna.</p>

  <h2 class="abs script-head testi-head">Testimonials</h2>
  <div class="abs btn testi-more">View All</div>
  <blockquote class="abs quote">"Lorem ipsum dolor sit amet, consectetuer adipiscing elit, sed diam nonummy nibh euismod tincidunt u ipsum dolor sit amet, consectetuer adipiscing elit, sed diam nonummy nibh euismod tincidunt ut laoreet dolore magna."<cite>— Daniel Marsh</cite></blockquote>
  <svg class="abs quote-tail" width="22" height="14" viewBox="0 0 22 14" aria-hidden="true"><path d="M0 1H22L6 13Z" fill="#fff" stroke="#e1e1e1" stroke-width="2"/><path d="M1 0H21V2H1Z" fill="#fff"/></svg>
</main>

<footer>
  <div class="abs footer"></div>
  <div class="abs footer-links">Halvenor Associates<span class="sep">|</span>Recruitment<span class="sep">|</span>Press<span class="sep">|</span>Imprint<span class="sep">|</span>Contact Us</div>
  <div class="abs copyright">© 2013 Halvenor Associates Ltd - All Rights Reserved.</div>
  <svg class="abs footer-globes" viewBox="0 0 122 60" role="img" aria-label="Pair of antique globe illustrations">
    <circle cx="30" cy="30" r="28" fill="url(#globe)" stroke="#c9a233" stroke-width="3"/>
    <circle cx="92" cy="30" r="28" fill="url(#globe)" stroke="#c9a233" stroke-width="3"/>
  </svg>
  <div class="abs footer-name">Halvenor Associates</div>
</footer>
</body>
</html>
```